We need to book cover designed for publishing on Parvello.
Needs to be for a book size 6" x 9" (15.24 x 22.86 cm).
Australian Financial Planning business
Title: "Quiet Harbour: A guide to retirement planning"
Covers attached via the PDF file.

Ultimately, this cover should convey the financial planner is a steady pair of hands and is a worthy read for trusted financial advice.

The text may need to be updated after the design has been created, so flexibility to update some of the text is required.

Target Market(s)

Australian Retirees (Financial Planning Book) - will be read by individuals 50 years and older

Industry/Entity Type

Finance, Financial Planning

Colors

Designer to choose colors to be used in the design.

Requirements
Must have
• Design suitable for Parvello publishing. Needs to be for a book size 6" x 9" (15.24 x 22.86 cm). Easy to identify cover, place on the back of the cover for an image of myself and company logo.
Nice to have
• Design the book cover with similar colors used in our logo (Blue #08387B and Gold #BC9C22)

```html
<!DOCTYPE html>
<html lang="en">
<head>
<meta charset="utf-8">
<title>Quiet Harbour – Book Cover</title>
<link href="https://fonts.googleapis.com/css2?family=Marcellus&display=swap" rel="stylesheet">
<style>
  :root {
    --page-bg: #e6e6e6;
    --cover-white: #efefef;
    --gold-dark: #9a8450;
    --gold-light: #c3aa76;
    --gold-mid: #ad955f;
    --ink: #0d0d0d;
    --band-ink: #2a2418;
  }
  * { margin: 0; padding: 0; box-sizing: border-box; }
  html, body {
    width: 1200px;
    height: 800px;
    overflow: hidden;
    background: var(--page-bg);
  }
  .canvas {
    position: relative;
    width: 1200px;
    height: 800px;
  }
  .book-cover {
    position: absolute;
    left: 400px;
    top: 100px;
    width: 400px;
    height: 600px;
    background: var(--cover-white);
    font-family: "Marcellus", serif;
    text-align: center;
    overflow: hidden;
  }
  .tagline-band {
    height: 34px;
    background: linear-gradient(90deg, var(--gold-dark), var(--gold-light) 50%, var(--gold-dark));
    display: flex;
    align-items: center;
    justify-content: center;
  }
  .tagline {
    font-size: 9.6px;
    letter-spacing: 0.1px;
    color: var(--band-ink);
    white-space: nowrap;
  }
  .book-title {
    position: absolute;
    top: 86px;
    left: 0;
    width: 100%;
    font-weight: 400;
    line-height: 1;
    background: linear-gradient(90deg, var(--gold-dark), var(--gold-light) 50%, var(--gold-dark));
    -webkit-background-clip: text;
    background-clip: text;
    color: transparent;
  }
  .book-title .title-main { display: block; font-size: 60px; letter-spacing: 1px; }
  .book-title .title-second { display: block; font-size: 46px; margin-top: 6px; }
  .rule {
    position: absolute;
    left: 59px;
    width: 282px;
    height: 1.5px;
    background: var(--gold-mid);
  }
  .rule-top { top: 226px; }
  .rule-bottom { top: 352px; }
  .subtitle {
    position: absolute;
    top: 236px;
    left: 0;
    width: 100%;
    color: var(--ink);
    line-height: 1;
    font-weight: 400;
  }
  .subtitle .sub-lead { display: block; font-size: 23px; letter-spacing: 1px; }
  .subtitle .sub-mid { display: block; font-size: 34px; letter-spacing: 1px; margin-top: 6px; }
  .subtitle .sub-last { display: block; font-size: 41px; letter-spacing: 2px; margin-top: 3px; }
  .cover-art {
    position: absolute;
    top: 368px;
    left: 65px;
    width: 270px;
    height: 170px;
    background: radial-gradient(ellipse 45% 50% at 50% 48%, #c9a65a 0%, #a88a4e 45%, rgba(200,185,150,0.35) 75%, rgba(239,239,239,0) 100%);
  }
  .author-band {
    position: absolute;
    bottom: 0;
    left: 0;
    width: 100%;
    height: 57px;
    background: linear-gradient(90deg, var(--gold-dark), var(--gold-light) 50%, var(--gold-dark));
    display: flex;
    align-items: center;
    justify-content: center;
  }
  .author-name {
    font-size: 30px;
    color: var(--ink);
    letter-spacing: 0.5px;
    font-weight: 400;
  }
</style>
</head>
<body>
<div class="canvas">
  <article class="book-cover">
    <div class="tagline-band">
      <p class="tagline">HOW TO BUILD WEALTH AND PLAN FOR YOUR RETIREMENT IN AUSTRALIA</p>
    </div>
    <h1 class="book-title">
      <span class="title-main">QUIET</span>
      <span class="title-second">HARBOUR</span>
    </h1>
    <div class="rule rule-top"></div>
    <h2 class="subtitle">
      <span class="sub-lead">A GUIDE TO</span>
      <span class="sub-mid">RETIREMENT</span>
      <span class="sub-last">PLANNING</span>
    </h2>
    <div class="rule rule-bottom"></div>
    <div class="cover-art" role="img" aria-label="A golden egg resting in a gilded bird's nest"></div>
    <div class="author-band">
      <p class="author-name">ROWAN ELLERY</p>
    </div>
  </article>
</div>
</body>
</html>
```